Menu Design for Indian Restaurant

We are a new Indian restaurant, named Saffron Lantern Restaurant, looking for a sophisticated looking menu. It is a semi-formal dining restaurant with wooden tables and chairs and will have a focus on a creating a lively atmosphere. Environment-friendly products will be used, and the menu will be 100% vegetarian. There will be an emphasis on fresh, healthy and delicious food. We will be targeting vegans, vegetarians, health conscious people, people from all age groups, Indians, Australian's as well as other ethnic communities. We need a clean, simple, sophisticated design for the new restaurant menu. Attached is the restaurant logo for reference.

UPDATE:
- We have attached the menu
- We are not looking for any particular type of layout or size (open to suggests). Please suggest this after having a look at the menu contents. However, we will be having one formal menu to be used in the restaurant, and one in brochure form for distribution.
- There are no images at present. If you feel the need of images, please use sample images for now.

Thank you for the entries thus far.
Updates

Target Market(s)

All age groups from different nationalities

Industry/Entity Type

Indian Restaurant

Colors

Designer to choose colors to be used in the design.

Requirements
Nice to have
• This will be printed on environmentally friendly paper.

```html
<!DOCTYPE html>
<html lang="en">
<head>
<meta charset="utf-8">
<title>Saffron Lantern Restaurant – Menu</title>
<link href="https://fonts.googleapis.com/css2?family=Righteous&family=Tinos:ital,wght@0,400;0,700;1,400&display=swap" rel="stylesheet">
<style>
  :root {
    --paper: #f5f5f4;
    --paper-edge: #e9e9e8;
    --ink: #1f1f1f;
    --rule: #8a8a8a;
    --saffron: #f08a24;
    --motif: rgba(150, 150, 150, 0.10);
  }
  * { box-sizing: border-box; margin: 0; padding: 0; }
  html, body { width: 1200px; height: 777px; overflow: hidden; }
  body {
    background: radial-gradient(ellipse at 50% 45%, #fbfbfa 0%, var(--paper) 55%, var(--paper-edge) 100%);
    color: var(--ink);
    font-family: "Tinos", "Times New Roman", serif;
    font-size: 10.5px;
    line-height: 14px;
    position: relative;
  }
  .page { position: absolute; top: 0; width: 600px; height: 777px; }
  .page--left { left: 0; }
  .page--right { left: 600px; }
  .fold {
    position: absolute; left: 599px; top: 12px; bottom: 12px;
    border-left: 1.5px dashed var(--rule);
  }
  .motif {
    position: absolute; top: 40px; left: 130px; width: 360px; height: 700px;
    border-radius: 45% 45% 30% 30%;
    background: radial-gradient(ellipse at 50% 45%, var(--motif) 0%, rgba(150,150,150,0.04) 60%, transparent 75%);
  }
  .brand {
    position: absolute; top: 58px; left: 0; width: 600px;
    display: flex; justify-content: center; align-items: center; gap: 8px;
    font-family: "Tinos", "Times New Roman", serif;
    font-weight: 700; font-size: 20px; line-height: 24px; color: var(--ink);
  }
  .brand__dot { width: 12px; height: 12px; border-radius: 50%; background: var(--saffron); }
  .section { position: absolute; left: 18px; width: 564px; }
  .section__title {
    font-family: "Righteous", "Arial Black", sans-serif;
    font-size: 15px; line-height: 16px; letter-spacing: 0.6px;
    text-align: center; margin-bottom: 4px; font-weight: 400;
  }
  .section__note { text-align: center; font-style: italic; margin-bottom: 2px; }
  .cols { display: grid; grid-template-columns: 268px 268px; column-gap: 28px; }
  .col { display: flex; flex-direction: column; gap: 7px; }
  .page--right .col { gap: 8px; }
  .col--rows { gap: 9px; }
  .item__desc { display: block; }
  .item__line { display: flex; align-items: baseline; font-weight: 700; }
  .item__leader { flex: 1; border-bottom: 1.5px dotted var(--ink); margin: 0 4px; transform: translateY(-3px); }
  .item__price { font-weight: 700; }
  .item__line--plain { justify-content: flex-start; gap: 4px; }
</style>
</head>
<body>

<main class="page page--left">
  <div class="motif" role="img" aria-label="Faint ornamental elephant illustration in the background"></div>
  <div class="brand"><span class="brand__dot"></span>Saffron Lantern Restaurant</div>

  <section class="section" style="top:99px">
    <h2 class="section__title">MAINS (continued)</h2>
    <div class="cols">
      <div class="col">
        <div class="item"><span class="item__desc">Cottage cheese cubes butter sauce nuts cream tomato</span><span class="item__line">Paneer Makhani (Nuts)<span class="item__leader"></span><span class="item__price">19.9</span></span></div>
        <div class="item"><span class="item__desc">Fine crushed mustard leafs onion garlic ginger flavoured with mustard oil</span><span class="item__line">Sarso Ka Saag<span class="item__leader"></span><span class="item__price">15.9</span></span></div>
        <div class="item"><span class="item__desc">Baby eggplant spiced stuffed tomato ginger garlic</span><span class="item__line">Bagare Baingan (Seasonal)<span class="item__leader"></span><span class="item__price">16.9</span></span></div>
      </div>
      <div class="col">
        <div class="item"><span class="item__desc">Fresh mix vegetable in creamy nut gravy</span><span class="item__line">Vegetable Korma<span class="item__leader"></span><span class="item__price">16.9</span></span></div>
        <div class="item"><span class="item__desc">Fresh mix vegetable coconut milk curry leafs mustard</span><span class="item__line">Appam Korma<span class="item__leader"></span><span class="item__price">16.9</span></span></div>
        <div class="item"><span class="item__desc">Bitter gourd stuffed potatoes spice onion ginger garlic serve on gravy</span><span class="item__line">Bharela Karela<span class="item__leader"></span><span class="item__price">15.9</span></span></div>
      </div>
    </div>
  </section>

  <section class="section" style="top:238px">
    <h2 class="section__title">SAFFRON BANQUET</h2>
    <div class="item" style="width:268px"><span class="item__desc" style="white-space:nowrap">2 entrée, 4 mains, one rice, naan/ roti, pappadam, salad, riata One dessert of your choice</span><span class="item__line">Banquet for 4/6/8/12/24 people<span class="item__leader"></span><span class="item__price">24.9</span></span></div>
  </section>

  <section class="section" style="top:291px">
    <h2 class="section__title">THALI</h2>
    <div class="cols">
      <div class="col">
        <div class="item"><span class="item__desc">4 curry salad pickle rice yogurt 2 roti pappadam sweet</span><span class="item__line">Gujrati Thali<span class="item__leader"></span><span class="item__price">21.9</span></span></div>
        <div class="item"><span class="item__desc">4 curry salad pickle rice yogurt 2 roti pappadam sweet</span><span class="item__line">Temil Thali<span class="item__leader"></span><span class="item__price">21.9</span></span></div>
      </div>
      <div class="col">
        <div class="item"><span class="item__desc">4 curry salad pickle rice yogurt naan pappadam sweet</span><span class="item__line">Punjabi Thali<span class="item__leader"></span><span class="item__price">21.9</span></span></div>
      </div>
    </div>
  </section>

  <section class="section" style="top:379px">
    <h2 class="section__title">FLAVOURS OF RICE</h2>
    <div class="cols">
      <div class="col">
        <div class="item"><span class="item__desc">Basmati rice mustard seeds red chilli curry leafs lemon and coconut flavoured</span><span class="item__line">Chitranna<span class="item__leader"></span><span class="item__price">4.9</span></span></div>
        <div class="item"><span class="item__desc">Cumin bay leaf pepper corn cinnamon flavoured</span><span class="item__line">Pulao Rice<span class="item__leader"></span><span class="item__price">4.9</span></span></div>
      </div>
      <div class="col">
        <div class="item"><span class="item__desc">Basmati rice no gluten less starch</span><span class="item__line">Steamed Basmati Rice<span class="item__leader"></span><span class="item__price">3.9</span></span></div>
        <div class="item"><span class="item__desc">Seasonal vegetable cooked with basmati rice and Indian aroma spice</span><span class="item__line">Vegetable Biryani<span class="item__leader"></span><span class="item__price">15.9</span></span></div>
      </div>
    </div>
  </section>

  <section class="section" style="top:482px">
    <h2 class="section__title">TAWA BREADS AND TANDOORI BREAD</h2>
    <div class="cols" style="margin-top:8px">
      <div class="col col--rows">
        <span class="item__line">Chappati<span class="item__leader"></span><span class="item__price">1.9</span></span>
        <span class="item__line">Roti<span class="item__leader"></span><span class="item__price">2.9</span></span>
        <span class="item__line">Naan<span class="item__leader"></span><span class="item__price">3.9</span></span>
        <span class="item__line">Garlic Naan<span class="item__leader"></span><span class="item__price">3.9</span></span>
        <span class="item__line">Butter Naan<span class="item__leader"></span><span class="item__price">4.9</span></span>
      </div>
      <div class="col col--rows">
        <span class="item__line">Aloo Kulcha<span class="item__leader"></span><span class="item__price">4.9</span></span>
        <span class="item__line">Paneer Kulcha<span class="item__leader"></span><span class="item__price">5.9</span></span>
        <span class="item__line">Kashmiri Naan<span class="item__leader"></span><span class="item__price">5.9</span></span>
        <span class="item__line">Missi Roti<span class="item__leader"></span><span class="item__price">3.9</span></span>
        <span class="item__line">Makki Ki Roti<span class="item__leader"></span><span class="item__price">3.9</span></span>
      </div>
    </div>
  </section>

  <section class="section" style="top:612px">
    <h2 class="section__title">ACCOMPANIMENTS</h2>
    <div class="cols" style="margin-top:8px">
      <div class="col col--rows">
        <span class="item__line">Kachumber Salad<span class="item__leader"></span><span class="item__price">3.9</span></span>
        <span class="item__line">Green Salad<span class="item__leader"></span><span class="item__price">4.9</span></span>
        <span class="item__line">Onion Salad<span class="item__leader"></span><span class="item__price">3.9</span></span>
        <span class="item__line">Raita Cucumber<span class="item__leader"></span><span class="item__price">3.9</span></span>
        <span class="item__line">Raita Cucumber Carrots<span class="item__leader"></span><span class="item__price">3.9</span></span>
      </div>
      <div class="col col--rows">
        <span class="item__line">Pickle<span class="item__leader"></span><span class="item__price">2.9</span></span>
        <span class="item__line">Mango Chutney<span class="item__leader"></span><span class="item__price">3.9</span></span>
        <span class="item__line">Pappadam South (2pcs)<span class="item__leader"></span><span class="item__price">1.9</span></span>
        <span class="item__line">Paddam Black Pepper (2pcs)<span class="item__leader"></span><span class="item__price">1.9</span></span>
      </div>
    </div>
  </section>
</main>

<div class="fold"></div>

<main class="page page--right">
  <div class="motif" role="img" aria-label="Faint ornamental elephant illustration in the background"></div>
  <div class="brand"><span class="brand__dot"></span>Saffron Lantern Restaurant</div>

  <section class="section" style="top:99px">
    <h2 class="section__title">ENTREE (TAPAS)</h2>
    <div class="cols">
      <div class="col">
        <div class="item"><span class="item__desc">Crispy potatoes curry leaves lotus stem ginger fresh coriander fresh chilli spice croquets</span><span class="item__line">Kamal Kofta (4pcs)<span class="item__leader"></span><span class="item__price">6.9</span></span></div>
        <div class="item"><span class="item__desc">Fresh baby spinach ricotta cheese mash potatoes ginger fresh coriander fresh chilli patty</span><span class="item__line">Hara Kebab (4pcs)<span class="item__leader"></span><span class="item__price">6.9</span></span></div>
        <div class="item"><span class="item__desc">Crispy tangy piquant mustard flavoured cheddar ginger garlic cauliflower and broccoli</span><span class="item__line">Tandoori Fool (5pcs)<span class="item__leader"></span><span class="item__price">6.9</span></span></div>
        <div class="item"><span class="item__desc">Cup mushroom yogurt spice cheese fresh mint coriander onion capsicum</span><span class="item__line">Tandoori Mushrooms (4pcs)<span class="item__leader"></span><span class="item__price">7.9</span></span></div>
        <div class="item"><span class="item__desc">Vegetable stuffed pastry steamed serve with homemade chilli sauce</span><span class="item__line">Momos (6pcs)<span class="item__leader"></span><span class="item__price">6.9</span></span></div>
        <div class="item"><span class="item__desc">Vegetable momos , yoghurt, ginger , garlic cooked in clay oven</span><span class="item__line">Tandoori Momos (6pcs)<span class="item__leader"></span><span class="item__price">7.9</span></span></div>
      </div>
      <div class="col">
        <div class="item"><span class="item__desc">Pastry stuffed with mushrooms, steamed homemade chilli sauce</span><span class="item__line">Mushrooms Momos (6pcs)<span class="item__leader"></span><span class="item__price">6.9</span></span></div>
        <div class="item"><span class="item__desc">Cottage cheese gram flour mint chilli flavoured yogurt</span><span class="item__line">Paneer Tikka (4pcs)<span class="item__leader"></span><span class="item__price">7.9</span></span></div>
        <div class="item"><span class="item__desc">Chickpeas mince raw mango powder green sultana</span><span class="item__line">Kabuli Tiki (4pcs)<span class="item__leader"></span><span class="item__price">6.9</span></span></div>
        <div class="item"><span class="item__desc">Crispy pastry stuffed potatoes peas on chickpeas</span><span class="item__line">Samosa Chat (2pcs)<span class="item__leader"></span><span class="item__price">6.9</span></span></div>
        <div class="item"><span class="item__desc">Potato patty fresh coriander cumin seed pea flour on chickpeas</span><span class="item__line">Aloo Tikki Chat (2pcs)<span class="item__leader"></span><span class="item__price">6.9</span></span></div>
        <div class="item"><span class="item__desc">Crispy pastry lentil dumpling yogurt date and mint chutney</span><span class="item__line">Dhai Bhalla Papdi<span class="item__leader"></span><span class="item__price">6.9</span></span></div>
      </div>
    </div>
  </section>

  <section class="section" style="top:424px">
    <h2 class="section__title">BURGER PARADE</h2>
    <p class="section__note">Served with spicy potato fries</p>
    <div class="cols">
      <div class="col">
        <div class="item"><span class="item__desc">Vegetables potatoes patty beetroot carrot onion lettuce</span><span class="item__line">Grass Hopper<span class="item__leader"></span><span class="item__price">7.9</span></span></div>
      </div>
      <div class="col">
        <div class="item"><span class="item__desc">Potato cottage cheese patty tomato capsicum cucumber lettuce cheese</span><span class="item__line">Cheese Hopper<span class="item__leader"></span><span class="item__price">7.9</span></span></div>
      </div>
    </div>
  </section>

  <section class="section" style="top:506px">
    <h2 class="section__title">PIZZA</h2>
    <p class="section__note">Medium size</p>
    <div class="cols" style="margin-top:4px">
      <div class="col">
        <div class="item"><span class="item__desc">Pineapple capsicum marjoram pitted black olive tomato cheese</span><span class="item__line item__line--plain">Tropicana <span class="item__price">11.9</span></span></div>
        <div class="item"><span class="item__desc">Jalapeño capsicum tomato mushrooms black olive cheese</span><span class="item__line item__line--plain">Mexicana <span class="item__price">12.9</span></span></div>
        <div class="item"><span class="item__desc">Greek cheese capsicum red Kalamata olives onion tomato cheese</span><span class="item__line item__line--plain">Kalamata <span class="item__price">12.9</span></span></div>
      </div>
      <div class="col">
        <div class="item"><span class="item__desc">Sun dry tomato green olive artichoke fresh parsley cheese</span><span class="item__line item__line--plain">Siciliana <span class="item__price">12.9</span></span></div>
        <div class="item"><span class="item__desc">Cottage cheese tomato capsicum onion cheese</span><span class="item__line item__line--plain">Indiana <span class="item__price">12.9</span></span></div>
      </div>
    </div>
  </section>

  <section class="section" style="top:674px">
    <h2 class="section__title">ALL TIME FAVORITE</h2>
    <div class="item" style="width:268px"><span class="item__desc" style="white-space:nowrap">Chickpeas onion tomato ginger fresh coriander deep fried bread pickle</span><span class="item__line">Channa Bhatura (2pcs)<span class="item__leader"></span><span class="item__price">9.9</span></span></div>
  </section>
</main>

</body>
</html>
```